Coffee bag stamp design for new coffee brand

Stamp design that will be used like a label on a coffee package.
It must be a vector that can be produced as a stamp. Coffee bag is from brown craft paper. I upload image of this bag. Size of design is 80mm x 140mm.
I also uploaded two pictures for inspiration, but I will also appreciate new ideas.

Target Market(s)

Coffee lovers, who love to try new coffee. Also hipsters.

Colors

Designer to choose only greyscale colors for use in the design.

Requirements
Must have
• Some information about coffee must have:
Name: BRAZIL (the biggest font in that design)
Region: Santos
Altitude: 60 – 1200 m.n.m.
Variety: Arabica
Processing: unwashed

```html
<!DOCTYPE html>
<html lang="en">
<head>
<meta charset="utf-8">
<title>Halden Coffee – Brazil Stamp Label</title>
<link rel="stylesheet" href="https://fonts.googleapis.com/css2?family=Archivo+Black&family=Archivo:wght@400;700&display=swap">
<style>
  :root {
    --kraft: #c89c6d;
    --ink: #161310;
    --page: #c89c6d;
  }
  * { box-sizing: border-box; margin: 0; padding: 0; }
  html, body {
    width: 1200px;
    height: 800px;
    overflow: hidden;
    background: var(--page);
  }
  .canvas {
    position: relative;
    width: 1200px;
    height: 800px;
    background: var(--page);
    color: var(--ink);
    font-family: "Archivo", sans-serif;
  }
  .stamp-frame {
    position: absolute;
    left: 387px;
    top: 130px;
    width: 425px;
    height: 600px;
    border: 3px solid var(--ink);
  }
  .brand-mark {
    position: absolute;
    left: 50%;
    top: 130px;
    transform: translate(-50%, -50%);
    display: flex;
    align-items: center;
    gap: 12px;
    padding: 0 14px;
    background: var(--kraft);
  }
  .brand-dot {
    width: 34px;
    height: 34px;
    border: 4px solid var(--ink);
    border-radius: 50%;
  }
  .brand-name {
    font-family: "Archivo", sans-serif;
    font-weight: 700;
    font-size: 34px;
    letter-spacing: 0.5px;
    color: var(--ink);
    white-space: nowrap;
  }
  .variety {
    position: absolute;
    left: 22px;
    top: 178px;
    font-family: "Archivo", sans-serif;
    font-weight: 400;
    font-size: 42px;
    letter-spacing: 4px;
    line-height: 1;
    white-space: nowrap;
  }
  .origin {
    position: absolute;
    left: 20px;
    top: 238px;
    font-family: "Archivo Black", sans-serif;
    font-size: 90px;
    letter-spacing: 1px;
    line-height: 1;
    white-space: nowrap;
  }
  .detail-band {
    position: absolute;
    left: 4px;
    top: 354px;
    width: 412px;
    height: 104px;
    background: var(--ink);
    color: var(--kraft);
    padding: 8px 0 0 22px;
    font-family: "Archivo", sans-serif;
    font-weight: 700;
    font-size: 38px;
    letter-spacing: 3.5px;
    line-height: 48px;
  }
  .altitude {
    position: absolute;
    left: 0;
    right: 0;
    top: 500px;
    text-align: center;
    font-family: "Archivo", sans-serif;
    font-weight: 700;
    font-size: 36px;
    letter-spacing: 3px;
    line-height: 42px;
  }
</style>
</head>
<body>
  <main class="canvas">
    <section class="stamp-frame">
      <p class="variety">100% ARABICA</p>
      <h1 class="origin">BRAZIL</h1>
      <div class="detail-band">
        <p class="region">SANTOS</p>
        <p class="process">UNWASHED</p>
      </div>
      <p class="altitude">60–120<br>M.N.M.</p>
    </section>
    <div class="brand-mark">
      <span class="brand-dot"></span>
      <span class="brand-name">HALDEN COFFEE</span>
    </div>
  </main>
</body>
</html>
```